Business Card Design

Printing and photocopying solutions, computer sales, photocopier sales and service, stationery needs

We aim to be the best for reliability, knowledge, skilled technical ability and highly ethical in business dealings. We would like to present as professional and the key person for dealing with for all customers. We are based in the Solomon Islands and therefore part of a developing country where many services and infrastructures are not in place. We would like to be seen as leading the field with technology and advanced office support. We strongly support the community and education systems with our current services and are seeking to expand the reach to encompass other service offerings

Target Market(s)

Business, Schools, Government offices, Churches, Non-government organisations

Industry/Entity Type

Business

Contact Information for Business Card

Harbourline Print
harbourlineprint@mailbay.net
+677 7418902 +677 8257113
PO Box 9
Auki, Malaita Province
Solomon Islands

Requirements
Must have
• professional appearance. Some Blue colouring
Must have easy to read phone number so required the phone number to be large font

Must have Shop address as well
Shop 7, Tidewell Building
Auki, Malaita, Solomon Islands
Nice to have
• Keep simple and professional with appearance of the business card styles, use the back of the card for Logo and a list of the basic services that is offered from Harbourline Print

```html
<!DOCTYPE html>
<html lang="en">
<head>
<meta charset="utf-8">
<title>Harbourline Print — Business Card</title>
<link rel="stylesheet" href="https://fonts.googleapis.com/css2?family=Montserrat:wght@700&family=Open+Sans:wght@400;700&display=swap">
<style>
  :root {
    --page-bg: #eceff2;
    --card-bg: #ffffff;
    --ink: #1a1a1a;
    --ink-soft: #333333;
    --brand-blue: #1f6aa8;
    --brand-blue-deep: #0f4677;
    --sky-1: #f4f8fc;
    --sky-2: #b9d3ec;
    --sky-3: #4d8cc6;
    --decor-grey: #e3e3e3;
  }
  * { box-sizing: border-box; margin: 0; padding: 0; }
  html, body {
    width: 1200px; height: 784px; overflow: hidden;
    background: var(--page-bg);
  }
  .sheet {
    position: relative; width: 1200px; height: 784px;
    display: flex; align-items: center; justify-content: center; gap: 40px;
  }
  .card {
    position: relative; width: 540px; height: 308px;
    background: var(--card-bg);
    box-shadow: 0 6px 18px rgba(0,0,0,0.12);
    overflow: hidden;
  }
  .card-front__artwork {
    position: absolute; inset: 0;
    background:
      radial-gradient(ellipse at 45% 50%, var(--sky-1) 0%, var(--sky-2) 45%, transparent 75%),
      linear-gradient(135deg, var(--sky-1) 0%, var(--sky-2) 40%, var(--sky-3) 70%, var(--sky-1) 100%);
  }
  .card-back__decor {
    position: absolute; right: 40px; top: 60px;
    width: 150px; height: 150px;
    background: var(--decor-grey);
  }
  .brand {
    position: absolute; left: 40px; top: 62px;
    display: flex; align-items: center; gap: 14px;
  }
  .brand__mark {
    width: 42px; height: 42px; background: var(--brand-blue);
  }
  .brand__name {
    font-family: "Montserrat", sans-serif; font-weight: 700;
    font-size: 28px; letter-spacing: -0.5px; color: var(--ink);
  }
  .contact {
    position: absolute; left: 40px; top: 138px;
    list-style: none;
    font-family: "Open Sans", sans-serif; color: var(--ink-soft);
    font-size: 13px; line-height: 17px;
  }
  .contact__item { display: flex; align-items: flex-start; gap: 6px; margin-bottom: 3px; }
  .contact__icon { width: 14px; height: 14px; flex: none; margin-top: 2px; fill: var(--brand-blue); }
  .contact__item--phone { font-weight: 700; font-size: 17px; line-height: 21px; color: var(--ink); }
  .contact__item--phone .contact__icon { margin-top: 4px; }
</style>
</head>
<body>
<main class="sheet">
  <section class="card card-front" aria-label="Card front">
    <div class="card-front__artwork" role="img" aria-label="Abstract blue and white glass panels radiating outward from the centre"></div>
  </section>

  <section class="card card-back" aria-label="Card back">
    <div class="card-back__decor" aria-hidden="true"></div>

    <div class="brand">
      <span class="brand__mark" aria-hidden="true"></span>
      <span class="brand__name">Harbourline Print</span>
    </div>

    <ul class="contact">
      <li class="contact__item contact__item--phone">
        <svg class="contact__icon" viewBox="0 0 24 24" aria-hidden="true"><path d="M6.6 10.8a15.1 15.1 0 0 0 6.6 6.6l2.2-2.2a1 1 0 0 1 1-.25 11.4 11.4 0 0 0 3.6.6 1 1 0 0 1 1 1V20a1 1 0 0 1-1 1A17 17 0 0 1 3 4a1 1 0 0 1 1-1h3.5a1 1 0 0 1 1 1c0 1.25.2 2.45.6 3.6a1 1 0 0 1-.25 1z"/></svg>
        <span>+677 7418902</span>
      </li>
      <li class="contact__item contact__item--phone">
        <svg class="contact__icon" viewBox="0 0 24 24" aria-hidden="true"><path d="M6.6 10.8a15.1 15.1 0 0 0 6.6 6.6l2.2-2.2a1 1 0 0 1 1-.25 11.4 11.4 0 0 0 3.6.6 1 1 0 0 1 1 1V20a1 1 0 0 1-1 1A17 17 0 0 1 3 4a1 1 0 0 1 1-1h3.5a1 1 0 0 1 1 1c0 1.25.2 2.45.6 3.6a1 1 0 0 1-.25 1z"/></svg>
        <span>+677 8257113</span>
      </li>
      <li class="contact__item">
        <svg class="contact__icon" viewBox="0 0 24 24" aria-hidden="true"><path d="M2 5h20v14H2zm2 2v.5l8 5 8-5V7zm0 2.8V17h16V9.8l-8 5z"/></svg>
        <span>harbourlineprint@mailbay.net</span>
      </li>
      <li class="contact__item">
        <svg class="contact__icon" viewBox="0 0 24 24" aria-hidden="true"><path d="M12 3 2 12h3v8h5v-5h4v5h5v-8h3z"/></svg>
        <span>PO Box 9 Auki,<br>Malaita Province Solomon Islands</span>
      </li>
      <li class="contact__item">
        <svg class="contact__icon" viewBox="0 0 24 24" aria-hidden="true"><path d="M12 3 2 12h3v8h5v-5h4v5h5v-8h3z"/></svg>
        <span>Shop 7, Tidewell Building<br>Auki, Malaita, Solomon Islands</span>
      </li>
    </ul>
  </section>
</main>
</body>
</html>
```